Gym Menu

Hi,

I would like to create a menu for my fitness center/ Dance school.

I do have a picture of how i would like it to look like ill attach it down there and instead of the Mexican looking icons i would like to have gym related icons example (Bar bell, dumbbells, etc..)

The menu will consist of the following

Smoothies
- Lunar Picnic (20 SR)
(Kiwi, Pineapple, Banana, Grapes)
-Sunny Cascade (20 SR)
(Orange, Peach, Pineapple)
-Tidal Dawn (20 SR)
(Carrot, Mango, Orange)
-Plum Thunder (20 SR)
(Blackberry, Raspberry, Banana)
-Cool Breeze (20 SR)
( Lemonade, Mint)
-Cherry Meadows (20 SR)
(Lemonade, Strawberry, Mint)

Mean Green Juices

-Leafy Lass (20SR)
(Cucumber, Celery, Green Apple, Spinach, Lemon, Ginger)
-Roots Rock Out! (20 SR)
(Carrots, Apple, Beetroot)

Shake It Up

-Latte Frenzy (20 SR)
(Mocha, Skimmed Milk)

- Velvet Freeze
(Chocolate, Skimmed Milk)

-Top Fuel Flex

(Peanut Butter, Honey, Skimmed Milk, Banana) (20 SR)

Yummy Bites

- Zataar Croissant (10 SR)
- Cheese Croissant (10 SR)
- Plane Croissant (10 SR)
- Blueberry Muffin (7 SR)
- Chocolate Muffin (7 SR)
- Vanilla Muffin (7SR)
- Cookies (7 SR)
- Brownie (10 SR)
-Fresh Berry Popsicle (10 SR)
- Fresh Orange Popsicle (10 SR)

Make it Lite

-Garden Salad (15 SR)
-Greek Salad (15 SR)
-Ceaser Salad (15 SR)
-Italian Salad (15 SR)
- Tuna Sandwich (25 SR)
- Turkey Sandwich (25 SR)
- Chicken Sandwich (25 SR)
-Happy Harvest Cup (8SR)
- Mixed Nuts (10 SR)

Coffee and tea
- Americano (10 SR)
- Espresso (10 SR)
- Turkish Coffee (10 SR)
- Cappuccino (15 SR)
- Cafe Latte (15 SR)
-Hot Cacao (15 SR)
-Extra shor + 5SR

- Green Tea (10 SR)
- Earl Grey (10 SR)
- English Breakfast (10SR)

• The gyms color is orange ... i want this to be in the menu

the gyms name is valmora i also want this in big somewhere

Colors of the menu should be

Orange
Yellow
green
red

all shades

```html
<!DOCTYPE html>
<html lang="en">
<head>
<meta charset="utf-8">
<title>valmora menu</title>
<link href="https://fonts.googleapis.com/css2?family=Josefin+Sans:wght@200;300&family=Pathway+Gothic+One&family=Yellowtail&display=swap" rel="stylesheet">
<style>
  :root{
    --stage:#f6f6f4;
    --paper:#f2f0ea;
    --cover:#d9a40c;
    --orange:#df6418;
    --amber:#e6a21c;
    --yellow:#e9b825;
    --green:#8aa83a;
    --red:#c9412a;
    --ink:#5a5852;
    --muted:#7a776f;
    --white:#ffffff;
  }
  *{margin:0;padding:0;box-sizing:border-box}
  html,body{width:1200px;height:1000px;overflow:hidden;background:var(--stage)}
  .canvas{position:relative;width:1200px;height:1000px}
  .sprite{position:absolute;width:0;height:0;overflow:hidden}

  .panel{position:absolute;top:150px;width:270px;height:700px;background:var(--paper);overflow:hidden;box-shadow:0 2px 10px rgba(0,0,0,.08)}
  .cover{left:20px;background:var(--cover)}
  .spread{position:absolute;left:330px;top:150px;width:540px;height:700px;box-shadow:0 2px 10px rgba(0,0,0,.08)}
  .spread .panel{top:0;box-shadow:none}
  .inside-left{left:0}
  .inside-right{left:270px;border-left:1px solid #dcd9d0}
  .back{left:910px}

  .icon{position:absolute}
  .icon.orange{color:var(--orange)}
  .icon.amber{color:var(--amber)}
  .icon.yellow{color:var(--yellow)}
  .icon.red{color:var(--red)}
  .icon.green{color:var(--green)}

  .figure{position:absolute;border-radius:50%}
  .figure.orange{background:radial-gradient(circle at 40% 35%,var(--amber),var(--orange))}
  .figure.yellow{background:radial-gradient(circle at 40% 35%,#f1cd5a,var(--yellow))}
  .figure.amber{background:radial-gradient(circle at 40% 35%,var(--yellow),var(--amber))}
  .figure.fruit{border-radius:46% 46% 50% 50%;background:linear-gradient(160deg,var(--amber),var(--orange))}

  .cover-art{position:absolute;left:60px;top:40px;width:150px;height:230px;border-radius:70px 70px 80px 80px;background:rgba(255,255,255,.82)}
  .brand{position:absolute;left:0;width:100%;top:330px;text-align:center;font-family:"Josefin Sans",sans-serif;font-weight:200;font-size:64px;letter-spacing:2px;color:var(--white)}
  .brand-sub{position:absolute;left:0;width:100%;top:410px;text-align:center;font-family:"Yellowtail",cursive;font-size:40px;color:var(--white)}
  .cover-mark{position:absolute;left:50%;bottom:40px;transform:translateX(-50%);color:var(--white)}

  .section{position:absolute;font-family:"Pathway Gothic One",sans-serif;color:var(--ink)}
  .section h2{font-family:"Yellowtail",cursive;font-weight:400;font-size:20px;color:var(--orange);margin-bottom:4px;line-height:1.2}
  .section ul{list-style:none}
  .section li{font-size:12.5px;line-height:1.25;margin-bottom:2px}
  .section li::before{content:"- "}
  .section li span{display:block;padding-left:8px;font-size:11px;color:var(--muted)}
  .cols{display:flex;gap:14px}
</style>
</head>
<body>
<svg class="sprite" aria-hidden="true">
  <defs>
    <symbol id="dumbbell" viewBox="0 0 100 50">
      <rect x="4" y="12" width="12" height="26" rx="3" fill="currentColor"/>
      <rect x="16" y="6" width="14" height="38" rx="3" fill="currentColor"/>
      <rect x="30" y="21" width="40" height="8" fill="currentColor"/>
      <rect x="70" y="6" width="14" height="38" rx="3" fill="currentColor"/>
      <rect x="84" y="12" width="12" height="26" rx="3" fill="currentColor"/>
    </symbol>
    <symbol id="barbell" viewBox="0 0 120 50">
      <rect x="2" y="22" width="116" height="6" rx="3" fill="currentColor"/>
      <rect x="14" y="4" width="10" height="42" rx="3" fill="currentColor"/>
      <rect x="26" y="10" width="8" height="30" rx="3" fill="currentColor"/>
      <rect x="86" y="10" width="8" height="30" rx="3" fill="currentColor"/>
      <rect x="96" y="4" width="10" height="42" rx="3" fill="currentColor"/>
    </symbol>
    <symbol id="kettlebell" viewBox="0 0 100 110">
      <path d="M30 40 V28 a20 20 0 0 1 40 0 V40" fill="none" stroke="currentColor" stroke-width="12"/>
      <path d="M50 36 c28 0 44 20 44 40 c0 18 -10 30 -20 30 H26 c-10 0 -20 -12 -20 -30 c0 -20 16 -40 44 -40z" fill="currentColor"/>
      <circle cx="50" cy="74" r="17" fill="var(--paper)"/>
      <text x="50" y="81" text-anchor="middle" font-family="Pathway Gothic One, sans-serif" font-size="20" fill="currentColor">10</text>
    </symbol>
    <symbol id="plate" viewBox="0 0 60 60">
      <circle cx="30" cy="30" r="28" fill="currentColor"/>
      <circle cx="30" cy="30" r="17" fill="none" stroke="var(--paper)" stroke-width="3"/>
      <circle cx="30" cy="30" r="6" fill="var(--paper)"/>
    </symbol>
    <symbol id="stopwatch" viewBox="0 0 60 66">
      <rect x="24" y="0" width="12" height="7" rx="2" fill="currentColor"/>
      <circle cx="30" cy="38" r="26" fill="currentColor"/>
      <circle cx="30" cy="38" r="19" fill="var(--paper)"/>
      <path d="M30 38 V24 M30 38 L40 44" stroke="currentColor" stroke-width="4" stroke-linecap="round"/>
    </symbol>
    <symbol id="heart" viewBox="0 0 100 90">
      <path d="M50 86 C18 62 2 46 2 26 C2 12 14 2 27 2 C38 2 46 9 50 18 C54 9 62 2 73 2 C86 2 98 12 98 26 C98 46 82 62 50 86z" fill="currentColor"/>
      <polyline points="10,40 32,40 40,24 50,58 58,32 64,40 90,40" fill="none" stroke="var(--paper)" stroke-width="5" stroke-linejoin="round"/>
    </symbol>
    <symbol id="apple" viewBox="0 0 60 64">
      <path d="M30 16 C20 8 2 12 2 32 C2 50 14 62 22 62 C26 62 28 60 30 60 C32 60 34 62 38 62 C46 62 58 50 58 32 C58 12 40 8 30 16z" fill="currentColor"/>
      <path d="M30 16 C30 10 32 5 36 2" stroke="currentColor" stroke-width="3" fill="none"/>
      <path d="M34 10 C40 2 50 4 50 4 C48 12 40 14 34 10z" fill="var(--green)"/>
    </symbol>
    <symbol id="bottle" viewBox="0 0 40 70">
      <rect x="13" y="0" width="14" height="8" rx="2" fill="currentColor"/>
      <path d="M10 12 H30 L34 22 V66 a4 4 0 0 1 -4 4 H10 a4 4 0 0 1 -4 -4 V22z" fill="currentColor"/>
      <rect x="6" y="34" width="28" height="14" fill="var(--paper)" opacity=".7"/>
    </symbol>
    <symbol id="scale" viewBox="0 0 70 60">
      <rect x="2" y="4" width="66" height="54" rx="8" fill="currentColor"/>
      <path d="M16 26 a19 19 0 0 1 38 0z" fill="var(--paper)"/>
      <path d="M35 26 L42 14" stroke="currentColor" stroke-width="3" stroke-linecap="round"/>
    </symbol>
    <symbol id="bike" viewBox="0 0 100 80">
      <circle cx="78" cy="58" r="18" fill="none" stroke="currentColor" stroke-width="6"/>
      <path d="M14 76 H90 M30 76 L40 40 L72 40 L78 58 M40 40 L34 22 M26 22 H44 M72 40 L76 16 H86" fill="none" stroke="currentColor" stroke-width="6" stroke-linecap="round" stroke-linejoin="round"/>
      <circle cx="54" cy="58" r="6" fill="currentColor"/>
    </symbol>
    <symbol id="ball" viewBox="0 0 60 60">
      <circle cx="30" cy="30" r="28" fill="currentColor"/>
      <path d="M6 24 C22 30 38 30 54 22 M10 44 C24 40 40 42 52 46" fill="none" stroke="var(--paper)" stroke-width="3"/>
    </symbol>
    <symbol id="shoe" viewBox="0 0 80 44">
      <path d="M4 8 C14 8 20 14 30 14 L36 6 C50 18 66 20 74 26 C78 30 78 36 74 38 H8 C4 38 2 34 2 28z" fill="currentColor"/>
      <rect x="2" y="38" width="76" height="5" rx="2" fill="currentColor"/>
    </symbol>
    <symbol id="cup" viewBox="0 0 60 70">
      <path d="M6 14 H48 L42 66 H12z" fill="currentColor"/>
      <path d="M30 14 L40 0" stroke="currentColor" stroke-width="4"/>
    </symbol>
  </defs>
</svg>

<div class="canvas">

  <section class="panel cover">
    <div class="cover-art" role="img" aria-label="Large white illustration of a fruit and a shaker bottle"></div>
    <div class="brand">valmora</div>
    <div class="brand-sub">menu</div>
    <svg class="cover-mark" width="80" height="40" aria-hidden="true"><use href="#dumbbell" width="80" height="40"/></svg>
  </section>

  <div class="spread">
    <section class="panel inside-left">
      <svg class="icon orange" style="left:16px;top:30px" width="86" height="36" aria-hidden="true"><use href="#barbell" width="86" height="36"/></svg>
      <svg class="icon amber" style="left:40px;top:70px" width="30" height="30" aria-hidden="true"><use href="#plate" width="30" height="30"/></svg>
      <div class="section" style="left:110px;top:16px;width:150px">
        <h2>Smoothies</h2>
        <ul>
          <li>Lunar Picnic (20 SR)<span>(Kiwi, Pineapple, Banana, Grapes)</span></li>
          <li>Sunny Cascade (20 SR)<span>(Orange, Peach, Pineapple)</span></li>
        </ul>
      </div>
      <div class="section" style="left:16px;top:120px;width:125px">
        <ul>
          <li>Tidal Dawn (20 SR)<span>(Carrot, Mango, Orange)</span></li>
          <li>Plum Thunder (20 SR)<span>(Blackberry, Raspberry, Banana)</span></li>
          <li>Cool Breeze (20 SR)<span>(Lemonade, Mint)</span></li>
          <li>Cherry Meadows (20 SR)<span>(Lemonade, Strawberry, Mint)</span></li>
        </ul>
      </div>
      <svg class="icon yellow" style="left:145px;top:135px" width="115" height="127" aria-hidden="true"><use href="#kettlebell" width="115" height="127"/></svg>
      <svg class="icon red" style="left:18px;top:300px" width="40" height="43" aria-hidden="true"><use href="#apple" width="40" height="43"/></svg>
      <svg class="icon orange" style="left:70px;top:296px" width="56" height="48" aria-hidden="true"><use href="#scale" width="56" height="48"/></svg>
      <div class="figure amber" style="left:150px;top:290px;width:58px;height:58px" role="img" aria-label="Swimmer pictogram"></div>
      <div class="figure orange" style="left:212px;top:306px;width:42px;height:42px" role="img" aria-label="Stretching figure pictogram"></div>
      <div class="section" style="left:16px;top:365px;width:240px">
        <h2>Mean Green Juices</h2>
        <ul>
          <li>Leafy Lass (20 SR)<span>(Cucumber, Celery, Green Apple, Spinach, Lemon, Ginger)</span></li>
          <li>Roots Rock Out! (20 SR)<span>(Carrots, Apple, Beetroot)</span></li>
        </ul>
      </div>
      <div class="figure orange" style="left:30px;top:490px;width:80px;height:80px" role="img" aria-label="Weightlifter pictogram"></div>
      <svg class="icon yellow" style="left:130px;top:500px" width="126" height="63" aria-hidden="true"><use href="#dumbbell" width="126" height="63"/></svg>
      <div class="figure yellow" style="left:16px;top:600px;width:70px;height:70px" role="img" aria-label="Jump rope figure pictogram"></div>
      <svg class="icon orange" style="left:98px;top:625px" width="66" height="36" aria-hidden="true"><use href="#shoe" width="66" height="36"/></svg>
      <svg class="icon green" style="left:186px;top:600px" width="36" height="63" aria-hidden="true"><use href="#bottle" width="36" height="63"/></svg>
    </section>

    <section class="panel inside-right">
      <svg class="icon amber" style="left:16px;top:24px" width="80" height="34" aria-hidden="true"><use href="#barbell" width="80" height="34"/></svg>
      <svg class="icon orange" style="left:150px;top:16px" width="100" height="80" aria-hidden="true"><use href="#bike" width="100" height="80"/></svg>
      <svg class="icon orange" style="left:16px;top:75px" width="40" height="44" aria-hidden="true"><use href="#stopwatch" width="40" height="44"/></svg>
      <svg class="icon orange" style="left:62px;top:80px" width="36" height="36" aria-hidden="true"><use href="#plate" width="36" height="36"/></svg>
      <div class="section" style="left:110px;top:112px;width:150px">
        <h2>Shake It Up</h2>
        <ul>
          <li>Latte Frenzy (20 SR)<span>(Mocha, Skimmed Milk)</span></li>
          <li>Velvet Freeze (20 SR)<span>(Chocolate, Skimmed Milk)</span></li>
          <li>Top Fuel Flex (20 SR)<span>(Peanut Butter, Honey, Skimmed Milk, Banana)</span></li>
        </ul>
      </div>
      <div class="figure amber" style="left:16px;top:150px;width:80px;height:80px" role="img" aria-label="Flexed arm pictogram"></div>
      <div class="figure yellow" style="left:16px;top:300px;width:70px;height:70px" role="img" aria-label="Swimmer pictogram"></div>
      <svg class="icon amber" style="left:96px;top:322px" width="40" height="40" aria-hidden="true"><use href="#plate" width="40" height="40"/></svg>
      <div class="figure orange" style="left:160px;top:285px;width:90px;height:90px" role="img" aria-label="Barbell lifter pictogram"></div>
      <div class="section" style="left:16px;top:400px;width:245px">
        <h2>Yummy Bites</h2>
        <div class="cols">
          <ul>
            <li>Zataar Croissant (10 SR)</li>
            <li>Cheese Croissant (10 SR)</li>
            <li>Plain Croissant (10 SR)</li>
            <li>Blueberry Muffin (7 SR)</li>
            <li>Chocolate Muffin (7 SR)</li>
          </ul>
          <ul>
            <li>Vanilla Muffin (7 SR)</li>
            <li>Cookies (7 SR)</li>
            <li>Brownie (10 SR)</li>
            <li>Fresh Berry Popsicle (10 SR)</li>
            <li>Fresh Orange Popsicle (10 SR)</li>
          </ul>
        </div>
      </div>
      <div class="figure orange" style="left:20px;top:590px;width:84px;height:84px" role="img" aria-label="Sprinter pictogram"></div>
      <svg class="icon amber" style="left:118px;top:628px" width="44" height="44" aria-hidden="true"><use href="#ball" width="44" height="44"/></svg>
      <svg class="icon red" style="left:170px;top:590px" width="88" height="79" aria-hidden="true"><use href="#heart" width="88" height="79"/></svg>
    </section>
  </div>

  <section class="panel back">
    <div class="section" style="left:16px;top:16px;width:240px">
      <h2>Make it Lite</h2>
      <div class="cols">
        <ul>
          <li>Garden Salad (15 SR)</li>
          <li>Greek Salad (15 SR)</li>
          <li>Caesar Salad (15 SR)</li>
          <li>Italian Salad (15 SR)</li>
          <li>Tuna Sandwich (25 SR)</li>
        </ul>
        <ul>
          <li>Turkey Sandwich (25 SR)</li>
          <li>Chicken Sandwich (25 SR)</li>
          <li>Happy Harvest Cup (8 SR)</li>
          <li>Mixed Nuts (10 SR)</li>
        </ul>
      </div>
    </div>
    <div class="figure orange" style="left:24px;top:160px;width:96px;height:96px" role="img" aria-label="Bodybuilder pictogram"></div>
    <svg class="icon amber" style="left:160px;top:150px" width="86" height="86" aria-hidden="true"><use href="#ball" width="86" height="86"/></svg>
    <svg class="icon amber" style="left:24px;top:280px" width="44" height="44" aria-hidden="true"><use href="#plate" width="44" height="44"/></svg>
    <svg class="icon orange" style="left:92px;top:270px" width="60" height="52" aria-hidden="true"><use href="#scale" width="60" height="52"/></svg>
    <div class="figure orange" style="left:180px;top:262px;width:60px;height:60px" role="img" aria-label="Stretching figure pictogram"></div>
    <svg class="icon orange" style="left:20px;top:350px" width="72" height="84" aria-hidden="true"><use href="#cup" width="72" height="84"/></svg>
    <svg class="icon orange" style="left:80px;top:370px" width="74" height="79" aria-hidden="true"><use href="#apple" width="74" height="79"/></svg>
    <div class="figure amber" style="left:178px;top:345px;width:66px;height:66px" role="img" aria-label="Seated rower pictogram"></div>
    <svg class="icon yellow" style="left:176px;top:425px" width="76" height="38" aria-hidden="true"><use href="#dumbbell" width="76" height="38"/></svg>
    <div class="section" style="left:16px;top:485px;width:240px">
      <h2>Coffee and Tea</h2>
      <div class="cols">
        <ul>
          <li>Americano (10 SR)</li>
          <li>Espresso (10 SR)</li>
          <li>Turkish Coffee (10 SR)</li>
          <li>Cappuccino (15 SR)</li>
          <li>Cafe Latte (15 SR)</li>
        </ul>
        <ul>
          <li>Hot Cacao (15 SR)</li>
          <li>Extra shot + 5 SR</li>
          <li>Green Tea (10 SR)</li>
          <li>Earl Grey (10 SR)</li>
          <li>English Breakfast (10 SR)</li>
        </ul>
      </div>
    </div>
  </section>

</div>
</body>
</html>
```